Maple Ridge business card design

Card needs to include the following text/items:
Company Logo
Tobin Marsh
Phone # - 555-318-7642
service@mapleridgelandscaping.example
Lawn & landscape maintenance services

```html
<!DOCTYPE html>
<html lang="en">
<head>
<meta charset="utf-8">
<title>Maple Ridge Landscaping – Business Card</title>
<link rel="stylesheet" href="https://fonts.googleapis.com/css2?family=Cinzel:wght@500;700&family=Raleway:wght@400;500&display=swap">
<style>
  :root {
    --forest: #1f4d26;
    --paper: #ffffff;
    --ink: #2b2b2b;
    --rule: #3a3a3a;
    --mark: #4f8a3a;
    --stage: #e9ebe8;
  }
  * { box-sizing: border-box; margin: 0; padding: 0; }
  html, body {
    width: 1200px; height: 900px; overflow: hidden;
    background: var(--stage);
  }
  .canvas { position: relative; width: 1200px; height: 900px; }
  .card {
    position: absolute; left: 270px;
    width: 660px; height: 378px;
    background: var(--paper);
    overflow: hidden;
    box-shadow: 0 6px 18px rgba(0,0,0,.12);
  }
  .card--front { top: 48px; }
  .card--back { top: 474px; }

  /* Front */
  .front-band {
    position: absolute; left: 0; right: 0; bottom: 0; height: 170px;
    background: var(--forest);
  }
  .front-mark {
    position: absolute; left: 430px; top: 36px;
    width: 164px; height: 164px; border-radius: 50%;
    background: var(--mark);
  }
  .front-name {
    position: absolute; left: 64px; top: 256px;
    font-family: "Cinzel", serif; font-weight: 700;
    font-size: 34px; line-height: 1;
    color: var(--paper); white-space: nowrap;
  }

  /* Back */
  .back-band {
    position: absolute; left: 0; right: 0; bottom: 0; height: 68px;
    background: var(--forest);
    display: flex; align-items: center; padding-left: 62px;
  }
  .tagline {
    font-family: "Cinzel", serif; font-weight: 500;
    font-size: 19px; letter-spacing: 1px; color: var(--paper);
    text-transform: uppercase;
  }
  .person {
    position: absolute; left: 62px; top: 52px;
    font-family: "Cinzel", serif; font-weight: 700;
    font-size: 31px; color: var(--forest); letter-spacing: .5px;
  }
  .rule {
    position: absolute; left: 62px; top: 98px;
    width: 560px; height: 1px; background: var(--rule);
  }
  .contact {
    position: absolute; left: 62px; top: 116px;
    list-style: none;
    font-family: "Raleway", sans-serif; font-size: 16px; color: var(--ink);
  }
  .contact li { display: flex; align-items: center; gap: 10px; height: 28px; }
  .contact svg { width: 14px; height: 14px; flex: none; }
  .back-logo {
    position: absolute; right: 44px; top: 184px;
    display: flex; align-items: center; gap: 16px;
  }
  .back-logo .name {
    font-family: "Cinzel", serif; font-weight: 700;
    font-size: 24px; line-height: 1; color: var(--forest); white-space: nowrap;
  }
  .back-logo .mark {
    width: 96px; height: 96px; border-radius: 50%;
    background: var(--mark); flex: none;
  }
</style>
</head>
<body>
<main class="canvas">
  <section class="card card--front" aria-label="Card front">
    <div class="front-band"></div>
    <div class="front-mark" aria-hidden="true"></div>
    <h1 class="front-name">Maple Ridge Landscaping</h1>
  </section>

  <section class="card card--back" aria-label="Card back">
    <h2 class="person">Tobin Marsh</h2>
    <div class="rule"></div>
    <ul class="contact">
      <li>
        <svg viewBox="0 0 24 24" aria-hidden="true"><path fill="#1f4d26" d="M6.6 10.8a15.1 15.1 0 0 0 6.6 6.6l2.2-2.2a1 1 0 0 1 1-.25 11.4 11.4 0 0 0 3.6.57 1 1 0 0 1 1 1V20a1 1 0 0 1-1 1A17 17 0 0 1 3 4a1 1 0 0 1 1-1h3.5a1 1 0 0 1 1 1c0 1.25.2 2.45.57 3.57a1 1 0 0 1-.25 1z"/></svg>
        555-318-7642
      </li>
      <li>
        <svg viewBox="0 0 24 24" aria-hidden="true"><rect x="2" y="5" width="20" height="14" fill="#1f4d26"/><path d="M2 5l10 8 10-8" fill="none" stroke="#fff" stroke-width="1.6"/></svg>
        service@mapleridgelandscaping.example
      </li>
    </ul>
    <div class="back-logo">
      <p class="name">Maple Ridge Landscaping</p>
      <div class="mark" aria-hidden="true"></div>
    </div>
    <div class="back-band">
      <p class="tagline">Lawn &amp; Landscape Maintenance Services</p>
    </div>
  </section>
</main>
</body>
</html>
```